Buchcover für einen Thriller gesucht
Super Cover, sehr viele Entwürfe.
Zielgruppe
Ich bin ein Thrillerautor, meine Zielgruppe sind Leser zwischen 29 und 55 Jahren. Leser sind in der Regel vorwiegend weiblich, jedoch sollte das Buchcover nicht zu weiblich aussehen.
Aufgabenstellung
Das Cover zwingend zum Inhalt passen. Thema ist ein Thriller mit übersinnlichen Elementen. Leseprobe und Exposé mit Inhaltsangabe und allen relevanten Daten ist in den Dateiuploads enthalten. Weiterhin hängt eine Covervorlage für die Maße an. Mir ist insbesondere das Frontcover wichtig. Buchrückseite und Buchrücken würde ich mir zur Not allein anpassen. In der Masse der bei Bücherhain angebotenen Bücher sollte das Cover hervorstechen.
Buchcovertrends 2018, falls interessant: https://kurz.example/7RqTxw

```html
<!DOCTYPE html>
<html lang="de">
<head>
<meta charset="utf-8">
<title>Der Schrank im Flur – Horrorroman</title>
<link rel="stylesheet" href="https://fonts.googleapis.com/css2?family=Rubik+Dirt&family=Alegreya:wght@400&family=Oswald:wght@600&display=swap">
<style>
  :root {
    --wall-dark: #0b0908;
    --wall-mid: #1f1a16;
    --wall-warm: #5a3a22;
    --glow: #f6b45a;
    --floor-top: #3a3633;
    --floor-bottom: #141210;
    --title: #e4e1dc;
    --subtitle: #9d9a96;
    --author: #ffffff;
  }
  html, body {
    margin: 0;
    padding: 0;
    width: 800px;
    height: 1200px;
    overflow: hidden;
    background: var(--wall-dark);
  }
  .cover {
    position: relative;
    width: 800px;
    height: 1200px;
    overflow: hidden;
  }
  .cover-backdrop {
    position: absolute;
    inset: 0;
    background:
      radial-gradient(ellipse 160px 200px at 391px 150px, rgba(246,180,90,0.95) 0%, rgba(200,120,60,0.45) 30%, rgba(90,58,34,0.2) 65%, transparent 100%),
      radial-gradient(ellipse 520px 520px at 391px 180px, rgba(90,58,34,0.55) 0%, transparent 70%),
      linear-gradient(to bottom, var(--wall-mid) 0%, #15110f 45%, var(--wall-dark) 83%);
  }
  .cover-floor {
    position: absolute;
    left: 0;
    right: 0;
    top: 996px;
    bottom: 0;
    background: linear-gradient(to bottom, var(--floor-top) 0%, #26231f 45%, var(--floor-bottom) 100%);
  }
  .cover-title {
    position: absolute;
    left: 0;
    top: 0;
    width: 800px;
    height: 640px;
  }
  .cover-title text {
    font-family: "Rubik Dirt", "Impact", sans-serif;
    fill: var(--title);
  }
  .cover-genre {
    position: absolute;
    left: 378px;
    top: 572px;
    margin: 0;
    font-family: "Alegreya", Georgia, serif;
    font-size: 37px;
    letter-spacing: 0.5px;
    color: var(--subtitle);
  }
  .cover-author {
    position: absolute;
    left: 0;
    width: 800px;
    top: 1096px;
    margin: 0;
    text-align: center;
    font-family: "Oswald", "Arial Narrow", sans-serif;
    font-weight: 600;
    font-size: 36px;
    letter-spacing: 3px;
    color: var(--author);
  }
</style>
</head>
<body>
  <main class="cover">
    <div class="cover-backdrop" role="img" aria-label="Dunkle Holzbretterwand, oben hängt eine leuchtende Glühbirne mit warmem Licht"></div>
    <div class="cover-floor" role="img" aria-label="Dunkler, verwitterter Holzboden"></div>

    <svg class="cover-title" viewBox="0 0 800 640" aria-label="Der Schrank im Flur">
      <text x="105" y="271" font-size="92" textLength="184" lengthAdjust="spacingAndGlyphs">DER</text>
      <text x="40" y="413" font-size="156" textLength="729" lengthAdjust="spacingAndGlyphs">SCHRANK</text>
      <text x="191" y="518" font-size="92" textLength="112" lengthAdjust="spacingAndGlyphs">IM</text>
      <text x="335" y="556" font-size="140" textLength="354" lengthAdjust="spacingAndGlyphs">FLUR</text>
    </svg>

    <p class="cover-genre">Horrorroman</p>
    <p class="cover-author">JONAS WIRTH</p>
  </main>
</body>
</html>
```